Canadian Christian Church needs design for new sermon series

A graphic design for our series and an invitation card to invite people to the series. Check design brief for more detailed information. Target audience: young families and young adults. Looking for a creative design that will get people's attention and create interest. See design brief for copy of design purchased for previous series.
Updates
entered Apr 4 incorrectly. Need a week to receive and review designs, and today is Apr 2/19. Thanks!
Target Market(s)
young families and young adults
Colors
Designer to choose colors to be used in the design.
Look and feel

```html
<!DOCTYPE html>
<html lang="en">
<head>
<meta charset="utf-8">
<title>Messy – Sermon Series Invitation Card</title>
<link rel="stylesheet" href="https://fonts.googleapis.com/css2?family=Open+Sans:wght@400;700&family=Merriweather:wght@700&family=Comfortaa:wght@400&family=Oswald:wght@300&display=swap">
<style>
  :root {
    --page: #d9d4cf;
    --card-light: #7a6470;
    --card-mid: #64505c;
    --card-dark: #4f3c4a;
    --band: #3b2a3a;
    --photo-dark: #2c2224;
    --photo-warm: #7a4a32;
    --text: #ffffff;
    --text-soft: #f1e9ee;
    --rule: #e8dde4;
    --accent: #e8902a;
  }
  * { box-sizing: border-box; margin: 0; padding: 0; }
  html, body { width: 1200px; height: 1200px; overflow: hidden; }
  body { background: var(--page); position: relative; font-family: "Open Sans", sans-serif; color: var(--text); }

  .card {
    position: absolute; left: 260px; width: 680px; height: 534px; overflow: hidden;
    background: radial-gradient(ellipse at 70% 40%, var(--card-light), var(--card-mid) 55%, var(--card-dark));
    box-shadow: 0 6px 18px rgba(0,0,0,.25);
  }
  .card--front { top: 50px; }
  .card--back { top: 616px; }

  /* front */
  .front__photo {
    position: absolute; left: 0; top: 0; width: 400px; height: 427px;
    background: linear-gradient(160deg, var(--photo-dark) 0%, #3a2c30 45%, var(--photo-warm) 80%, rgba(122,74,50,0) 100%);
    -webkit-mask-image: linear-gradient(90deg, #000 70%, transparent 100%);
            mask-image: linear-gradient(90deg, #000 70%, transparent 100%);
  }
  .brand {
    position: absolute; display: flex; flex-direction: column; align-items: center; gap: 6px;
    font-family: "Oswald", sans-serif; font-weight: 300; color: var(--text-soft);
  }
  .brand__dot { width: 60px; height: 60px; border-radius: 50%; background: var(--accent); }
  .brand--front { right: 36px; top: 42px; font-size: 15px; }
  .brand--back { left: 428px; top: 350px; font-size: 12px; }
  .brand--back .brand__dot { width: 50px; height: 50px; }

  .front__title {
    position: absolute; right: 34px; top: 300px;
    font-size: 104px; font-weight: 700; line-height: 1; letter-spacing: -2px;
  }
  .front__band {
    position: absolute; left: 0; top: 427px; width: 100%; height: 86px; background: var(--band);
    display: flex; align-items: center; justify-content: center;
  }
  .front__tagline { font-family: "Merriweather", serif; font-weight: 700; font-size: 44px; color: var(--text-soft); }

  /* back */
  .back__intro { position: absolute; top: 34px; width: 100%; text-align: center; font-weight: 700; font-size: 22px; }
  .back__time { position: absolute; top: 64px; width: 100%; text-align: center; font-weight: 700; font-size: 43px; letter-spacing: .5px; }
  .col { position: absolute; top: 139px; }
  .col--sermons { left: 47px; width: 240px; }
  .col--features { left: 393px; width: 240px; }
  .col__head {
    height: 59px; border-top: 1.5px solid var(--rule); border-bottom: 1.5px solid var(--rule);
    display: flex; align-items: center; justify-content: center; text-align: center;
    font-weight: 700; font-size: 23px; line-height: 1;
  }
  .list {
    list-style: none; margin-top: 27px; font-family: "Comfortaa", sans-serif; font-size: 14.5px; color: var(--text-soft);
  }
  .col--sermons .list { margin-left: -8px; width: 340px; }
  .col--features .list { margin-left: 38px; }
  .list li { height: 26px; display: flex; align-items: center; }
  .list li::before { content: "†"; font-family: "Open Sans", sans-serif; margin-right: 9px; font-size: 15px; }
  .list .date { display: inline-block; width: 90px; }

  .back__footer {
    position: absolute; left: 0; bottom: 0; width: 100%; height: 72px; background: var(--band);
    display: flex; flex-direction: column; align-items: center; justify-content: center; gap: 5px;
    font-weight: 700; color: var(--text-soft);
  }
  .back__footer .address { font-size: 14.5px; }
  .back__footer .contact { font-size: 12.5px; }
</style>
</head>
<body>

<section class="card card--front">
  <div class="front__photo" role="img" aria-label="Photograph of a closed leather-bound Bible with a gold cross on its cover"></div>
  <div class="brand brand--front">
    <span class="brand__dot"></span>
    <span class="brand__name">Maple Grove Family Church</span>
  </div>
  <h1 class="front__title">Messy</h1>
  <div class="front__band"><p class="front__tagline">Joining God in the Mess</p></div>
</section>

<section class="card card--back">
  <p class="back__intro">The Time Of The Services,</p>
  <p class="back__time">Sundays @ 10:30</p>

  <div class="col col--sermons">
    <h2 class="col__head">Dates &amp; Sermon<br>Names</h2>
    <ul class="list">
      <li><span class="date">April 28th</span>: “We Made This Mess”</li>
      <li><span class="date">May 5th</span>: “Bless in the Mess”</li>
      <li><span class="date">May 12th</span>: “Born into the Mess”</li>
      <li><span class="date">May 19th</span>: “Messy Work”</li>
      <li><span class="date">May 26th</span>: “Messy Church”</li>
      <li><span class="date">June 2nd</span>: “Messy Hospitality”</li>
      <li><span class="date">June 9th</span>: TBD</li>
      <li><span class="date">June 16th</span>: “Messy within Boundaries”</li>
    </ul>
  </div>

  <div class="col col--features">
    <h2 class="col__head">Featuring</h2>
    <ul class="list">
      <li>Staffed nursery</li>
      <li>children’s program</li>
      <li>Coffee &amp; snacks</li>
      <li>Everyone welcome</li>
    </ul>
  </div>

  <div class="brand brand--back">
    <span class="brand__dot"></span>
    <span class="brand__name">Maple Grove Family Church</span>
  </div>

  <footer class="back__footer">
    <p class="address">Location – 1875 Cedar Line East Brampton, ON L6T 2K4</p>
    <p class="contact">Phone – 905.555.0148 | Email-info@mgfamilychurch.ca | Website-www.mgfamilychurch.ca</p>
  </footer>
</section>

</body>
</html>
```